R.T. Wexmoor Electrical work flyer

I need a flyer design to help generate some extra work. I'm more than happy for a designer to play around with pictures, text, headings, boarders. The flyer will be double sided A4 size.
We specialize in Residential, Commercial, & Industrial Electrical works including PV Solar System Designs & Installations, Maintenance, System Checks & Upgrades, Mains Upgrades, Overhead & Underground, Switchboard Installations & Upgrades, Safety Switches, Spa & Pool connections, LED Lighting solutions, Energy Audit Checks, Fans & Air Conditioning, Hi-bay Lighting, Carpark Lighting, Data Points, Comms Racks, New Home Builds, Office Fitouts ...
We pride ourselves on always doing a great job, guaranteed workmanship, competitive pricing, & leaving the site clean.
Call Derek for a quote on any of your electrical needs
Mobile:0418 736 204
Email: rtwexmoorelectrical@quillmail.test
PO Box 58
Brambleton Vale VIC 3179

LEN: 38517
NRB Accreditation: A3182609

I've added my company logo & some pics, photo's & electrical / solar brand logos that can be used but not a must. I'm more than happy if you can find better pics.

Target Market(s)

Office, Factory & Home Owners

Industry/Entity Type

Electrical

Font styles to use
Serif
Sans Serif

Requirements
Must have
• eye catchy design with not to much information overload.
• Just aiming for people to call up for quotes etc.
Nice to have
• My company logo, electrical & solar works available
Should not have
• pictures of kids

```html
<!DOCTYPE html>
<html lang="en">
<head>
<meta charset="utf-8">
<title>R.T. Wexmoor Electrical – Flyer</title>
<link href="https://fonts.googleapis.com/css2?family=Didact+Gothic&family=Montserrat:wght@300;400;500;600&family=Open+Sans:wght@400;700&display=swap" rel="stylesheet">
<style>
  :root{
    --green:#4db848;
    --green-dark:#3fa43b;
    --ink:#2b2b2b;
    --text:#333333;
    --paper:#ffffff;
    --backdrop:#d2d3d5;
  }
  *{box-sizing:border-box;margin:0;padding:0}
  html,body{width:1200px;height:826px;overflow:hidden}
  body{background:var(--backdrop);position:relative;font-family:"Montserrat",sans-serif;color:var(--text)}
  .page{position:absolute;top:59px;width:504px;height:713px;background:var(--paper);box-shadow:2px 3px 6px rgba(0,0,0,.35);overflow:hidden}
  .page--front{left:46px}
  .page--back{left:649px}

  .photo-grid{position:absolute;left:0;top:0;width:504px;height:334px;display:grid;grid-template-columns:repeat(3,1fr);grid-template-rows:repeat(2,1fr);gap:1px;background:#fff}
  .photo{width:100%;height:100%}
  .photo--boardroom{background:linear-gradient(160deg,#e8e6e3,#8a8079 70%,#3a2c26)}
  .photo--carpark{background:linear-gradient(180deg,#0e1524,#2a3140 60%,#4a4a50)}
  .photo--warehouse{background:linear-gradient(180deg,#9ea5ad,#d6d8da 60%,#e9eaeb)}
  .photo--solar{background:linear-gradient(180deg,#6e9ed8,#a9c4e4 40%,#3c4f6c 60%,#1f2c45)}
  .photo--kitchen{background:linear-gradient(160deg,#f1eef0,#b8a8c4 50%,#5d5360)}
  .photo--pool{background:linear-gradient(180deg,#0a0f18,#1d2a45 45%,#2f5fc4 75%,#1a3a8a)}

  .quote-callout{position:absolute;left:0;top:320px;width:431px;height:125px;background:var(--green);border-radius:0 24px 24px 0;color:#fff;text-align:center;padding-top:20px}
  .quote-callout__lead{font-weight:300;font-size:19.5px;letter-spacing:1.6px;line-height:24px}
  .quote-callout__phone{font-weight:300;font-size:29px;letter-spacing:.5px;margin-top:6px}

  .brand{position:absolute;display:flex;align-items:center}
  .brand__dot{border-radius:50%;flex:none}
  .brand__name{font-weight:500;line-height:1;letter-spacing:2px;white-space:nowrap}
  .brand__name span{display:block}

  .front-brand{left:55px;top:493px}
  .front-brand .brand__dot{width:100px;height:100px;background:var(--green);margin-right:22px}
  .front-brand .brand__name{color:#3a3a3a;font-size:40px}
  .front-brand .brand__name span+span{margin-top:8px;font-size:46px;letter-spacing:4px}

  .dot-rule{position:absolute;height:6px;background-image:radial-gradient(circle,var(--green) 2.6px,transparent 3px);background-size:15.5px 6px;background-repeat:repeat-x}
  .front-rule{left:178px;top:621px;width:342px}
  .back-rule{left:158px;top:173px;width:310px}

  .address{position:absolute;right:18px;top:645px;font-size:19.5px;font-weight:400;color:#222}
  .licence-bar{position:absolute;left:98px;bottom:0;width:406px;height:37px;background:var(--green);border-radius:14px 0 0 0;color:#fff;font-size:16px;display:flex;align-items:center;justify-content:center}

  .back-banner{position:absolute;left:43px;top:31px;width:461px;height:131px;background:var(--green);border-radius:28px 0 0 28px;display:flex;align-items:center;padding-left:28px}
  .back-banner .brand__dot{width:92px;height:92px;background:#fff;margin-right:24px}
  .back-banner .brand__name{color:#fff;font-size:34px;letter-spacing:1.5px}
  .back-banner .brand__name span+span{margin-top:8px;font-size:42px;letter-spacing:3px}

  .services{position:absolute;left:40px;top:208px;width:425px;font-family:"Didact Gothic",sans-serif;font-size:14px;line-height:18.4px;color:#222}
  .services__line{display:block;white-space:nowrap;text-align:justify;text-align-last:justify}
  .services__line--end{text-align-last:left}
  .pride{position:absolute;left:42px;top:390px}
  .pride__title{font-family:"Open Sans",sans-serif;font-weight:700;color:var(--green);font-size:19.5px}
  .pride__list{list-style:none;font-family:"Open Sans",sans-serif;font-size:16.5px;line-height:19.3px;color:#222}
  .pride__list li::before{content:"- "}
  .bulb-art{position:absolute;left:305px;top:399px;width:160px;height:84px;border-radius:42px 18px 18px 42px;background:radial-gradient(circle at 35% 45%,#bfe0ff,#4a8fd4 55%,#2b5fa0)}

  .partner-row{position:absolute;left:30px;top:511px;width:450px;height:26px;display:flex;align-items:center;justify-content:space-between}
  .partner-badge{height:18px;background:#cfcfcf;border-radius:3px}
  .partner-badge--a{width:68px;background:#8cc63f}
  .partner-badge--b{width:74px;background:#3dcd58}
  .partner-badge--c{width:66px;background:#f3a33a}
  .partner-badge--d{width:66px;height:20px;border-radius:10px;background:#e2231a}
  .partner-badge--e{width:62px;background:#c8102e}
  .partner-badge--f{width:26px;height:26px;background:#1d4f91;border-radius:0}
  .partner-badge--g{width:34px;background:#333}

  .site-photos{position:absolute;left:0;top:545px;width:504px;height:168px;display:grid;grid-template-columns:repeat(3,1fr);gap:2px;background:#fff}
  .photo--switchboard{background:linear-gradient(90deg,#a9b0b3,#e3e6e6 50%,#8e9598)}
  .photo--roof-array{background:linear-gradient(180deg,#a7c6e6,#dfe8ef 35%,#7b8795 65%,#3e4c5e)}
  .photo--inverter{background:linear-gradient(120deg,#c9cbcc,#8d9499 50%,#2f4b8c)}
  .email-bar{position:absolute;left:0;bottom:0;width:405px;height:37px;background:var(--green);border-radius:0 14px 0 0;color:#fff;font-size:16.5px;display:flex;align-items:center;padding-left:52px}
</style>
</head>
<body>
  <section class="page page--front">
    <div class="photo-grid">
      <div class="photo photo--boardroom" role="img" aria-label="Boardroom with recessed ceiling lighting"></div>
      <div class="photo photo--carpark" role="img" aria-label="Car park lit by pole lights at night"></div>
      <div class="photo photo--warehouse" role="img" aria-label="Warehouse with high-bay lighting"></div>
      <div class="photo photo--solar" role="img" aria-label="Rooftop solar panel array"></div>
      <div class="photo photo--kitchen" role="img" aria-label="Modern home interior with LED lighting"></div>
      <div class="photo photo--pool" role="img" aria-label="Illuminated swimming pool at night"></div>
    </div>
    <div class="quote-callout">
      <p class="quote-callout__lead">Call Derek for a quote on any of<br>your electrical needs</p>
      <p class="quote-callout__phone">0418 736 204</p>
    </div>
    <div class="brand front-brand">
      <div class="brand__dot"></div>
      <p class="brand__name"><span>R.T. Wexmoor</span><span>Electrical</span></p>
    </div>
    <div class="dot-rule front-rule"></div>
    <p class="address">Brambleton Vale VIC 3179, PO Box 58</p>
    <div class="licence-bar">LEN: 38517 / NRB Accreditation: A3182609</div>
  </section>

  <section class="page page--back">
    <div class="back-banner brand">
      <div class="brand__dot"></div>
      <p class="brand__name"><span>R.T. Wexmoor</span><span>Electrical</span></p>
    </div>
    <div class="dot-rule back-rule"></div>
    <p class="services">
      <span class="services__line">We specialize in Residential, Commercial, &amp; Industrial</span>
      <span class="services__line">Electrical works including PV Solar System Designs &amp;</span>
      <span class="services__line">Installations, Maintenance, System Checks &amp; Upgrades,</span>
      <span class="services__line">Mains Upgrades, Overhead &amp; Underground, Switchboard</span>
      <span class="services__line">Installations &amp; Upgrades, Safety Switches, Spa &amp; Pool</span>
      <span class="services__line">connections, LED Lighting solutions, Energy Audit Checks,</span>
      <span class="services__line">Fans &amp; Air Conditioning, Hi-bay Lighting, Carpark Lighting,</span>
      <span class="services__line">Data Points, Comms Racks, New Home Builds, Office</span>
      <span class="services__line services__line--end">Fitouts ...</span>
    </p>
    <div class="pride">
      <h2 class="pride__title">We pride ourselves:</h2>
      <ul class="pride__list">
        <li>on always doing a great job</li>
        <li>guaranteed workmanship</li>
        <li>competitive pricing</li>
        <li>leaving the site clean</li>
      </ul>
    </div>
    <div class="bulb-art" role="img" aria-label="Light bulb filled with solar panels and blue sky"></div>
    <div class="partner-row">
      <span class="partner-badge partner-badge--a"></span>
      <span class="partner-badge partner-badge--b"></span>
      <span class="partner-badge partner-badge--c"></span>
      <span class="partner-badge partner-badge--d"></span>
      <span class="partner-badge partner-badge--e"></span>
      <span class="partner-badge partner-badge--f"></span>
      <span class="partner-badge partner-badge--g"></span>
    </div>
    <div class="site-photos">
      <div class="photo photo--switchboard" role="img" aria-label="Open switchboard with circuit breakers"></div>
      <div class="photo photo--roof-array" role="img" aria-label="Solar panels installed on an industrial roof"></div>
      <div class="photo photo--inverter" role="img" aria-label="Wall-mounted solar inverter and isolators"></div>
    </div>
    <div class="email-bar">Email: rtwexmoorelectrical@quillmail.test</div>
  </section>
</body>
</html>
```